Corporate Business Card

Very professional, Modern, Not to busy, include phone address email, website
(253) 555-0174, 61807 19th Street N, Kent, WA 98517, marcus@kestrelbayholding.com, brelvanindustries.com

Target Market(s)

Manufacturing

Industry/Entity Type

Aero, machining, manufacturing, Off road racing

Contact Information for Business Card

Phone, address email, website

```html
<!DOCTYPE html>
<html lang="en">
<head>
<meta charset="utf-8">
<title>Brelvan Industries – Business Card</title>
<link rel="stylesheet" href="https://fonts.googleapis.com/css2?family=Josefin+Sans:wght@300;700&family=Montserrat:ital,wght@1,600&display=swap">
<style>
  :root {
    --navy: #314473;
    --red: #d93a3f;
    --paper: #ffffff;
    --ink-light: #ffffff;
  }
  * { margin: 0; padding: 0; box-sizing: border-box; }
  html, body { width: 1200px; height: 776px; overflow: hidden; background: var(--paper); }
  .card {
    position: relative;
    width: 1200px;
    height: 776px;
    background: var(--paper);
    font-family: "Josefin Sans", sans-serif;
    overflow: hidden;
  }
  .card__band { position: absolute; left: 0; top: 0; width: 1200px; height: 776px; }
  .brand-name {
    position: absolute;
    right: 42px;
    top: 70px;
    font-family: "Josefin Sans", sans-serif;
    font-weight: 700;
    font-size: 50px;
    line-height: 1;
    letter-spacing: 1px;
    color: var(--navy);
    text-transform: uppercase;
    text-align: right;
  }
  .person-name {
    position: absolute;
    left: 84px;
    top: 170px;
    font-weight: 700;
    font-size: 68px;
    line-height: 1;
    color: var(--navy);
  }
  .person-title {
    position: absolute;
    left: 106px;
    top: 238px;
    font-weight: 300;
    font-size: 35px;
    line-height: 1;
    color: var(--ink-light);
  }
  .contact-list { list-style: none; position: absolute; left: 42px; top: 390px; }
  .contact-item {
    display: flex;
    align-items: center;
    height: 76px;
    color: var(--ink-light);
    font-weight: 300;
    font-size: 39px;
  }
  .contact-item__icon { width: 56px; height: 56px; flex: none; margin-right: 30px; }
  .contact-item__text { line-height: 1; padding-top: 8px; }
  .website {
    position: absolute;
    left: 30px;
    top: 712px;
    font-family: "Montserrat", sans-serif;
    font-style: italic;
    font-weight: 600;
    font-size: 36px;
    line-height: 1;
    color: var(--navy);
  }
</style>
</head>
<body>
<div class="card">
  <svg class="card__band" viewBox="0 0 1200 776" aria-hidden="true">
    <polygon points="1136,223 1142,223 740,674 734,674" fill="var(--red)"/>
    <polygon points="0,223 1134,223 734,674 0,674" fill="var(--navy)"/>
  </svg>

  <div class="brand-name">Brelvan Industries</div>

  <div class="person-name">John Doe</div>
  <div class="person-title">Derector Finance</div>

  <ul class="contact-list">
    <li class="contact-item">
      <svg class="contact-item__icon" viewBox="0 0 56 56" aria-hidden="true">
        <circle cx="28" cy="28" r="25" fill="none" stroke="#fff" stroke-width="3"/>
        <path d="M24 14c-3 1-6 4-6 8 0 8 6 18 13 21 3 1 6-1 7-3l-5-6-3 2c-3-2-6-8-6-11l3-2-3-9z" fill="#fff"/>
      </svg>
      <span class="contact-item__text">(253) 555-0174</span>
    </li>
    <li class="contact-item">
      <svg class="contact-item__icon" viewBox="0 0 56 56" aria-hidden="true">
        <circle cx="28" cy="28" r="25" fill="none" stroke="#fff" stroke-width="3"/>
        <path d="M28 12c-7 0-11 5-11 11 0 8 11 21 11 21s11-13 11-21c0-6-4-11-11-11z" fill="#fff"/>
        <circle cx="28" cy="23" r="4" fill="var(--navy)"/>
      </svg>
      <span class="contact-item__text">61807 19th Street N, Kent, WA 98517</span>
    </li>
    <li class="contact-item">
      <svg class="contact-item__icon" viewBox="0 0 56 56" aria-hidden="true">
        <circle cx="28" cy="28" r="25" fill="none" stroke="#fff" stroke-width="3"/>
        <rect x="13" y="18" width="26" height="18" rx="2" fill="#fff"/>
        <path d="M13 19l13 10 13-10" fill="none" stroke="var(--navy)" stroke-width="2"/>
        <circle cx="39" cy="36" r="6" fill="#fff" stroke="var(--navy)" stroke-width="2"/>
      </svg>
      <span class="contact-item__text">marcus@kestrelbayholding.com</span>
    </li>
  </ul>

  <div class="website">www.brelvanindustries.com</div>
</div>
</body>
</html>
```